high end contractor

high end contracting company we do all phases of construction kitchen,bathrooms,etc... please look at my website before you design www.harborkeybuild.com

would love some sort of lines or logo or both

Industry/Entity Type

Construction

Contact Information for Business Card

company name: oak & meridian contracting address: 318 fenwick st kellerton ny 10618 email: harborkeybuild@mailbrook.com website: www.harborkeybuild.com office#: 914-208-3916 fax#: 914-208-5523 dominic valtersen mobile# 917-526-0389

```html
<!DOCTYPE html>
<html lang="en">
<head>
<meta charset="utf-8">
<title>Oak &amp; Meridian Contracting — Business Card</title>
<link rel="stylesheet" href="https://fonts.googleapis.com/css2?family=Jost:wght@400;500&family=Roboto+Condensed:wght@400;700&display=swap">
<style>
  :root {
    --teal: #1cb8a2;
    --teal-deep: #0e9f8b;
    --teal-light: #2cc8b3;
    --ink: #2f3132;
    --paper: #ffffff;
    --paper-shade: #ececec;
    --backdrop: #e6e6e3;
  }
  * { box-sizing: border-box; margin: 0; padding: 0; }
  html, body { width: 1200px; height: 1200px; overflow: hidden; }
  body {
    background: var(--backdrop);
    font-family: "Roboto Condensed", "Arial Narrow", sans-serif;
    position: relative;
  }
  .card {
    position: absolute;
    left: 150px;
    width: 900px;
    height: 514px;
    overflow: hidden;
    box-shadow: 0 6px 18px rgba(0,0,0,0.18);
  }
  .card--front { top: 56px; background: var(--paper); }
  .card--back {
    top: 630px;
    background: radial-gradient(ellipse at 65% 20%, var(--teal-light) 0%, var(--teal) 45%, var(--teal-deep) 100%);
  }

  /* Front */
  .front__header {
    position: absolute; left: 0; top: 0; width: 100%; height: 172px;
    background: linear-gradient(180deg, var(--paper-shade) 0%, var(--paper) 70%);
  }
  .front__accent {
    position: absolute; left: 0; top: 104px; width: 16px; height: 62px;
    background: var(--teal);
  }
  .company-name {
    position: absolute; left: 42px; top: 98px;
    font-family: "Jost", "Futura", sans-serif;
    font-weight: 500; font-size: 47px; letter-spacing: 0.5px;
    color: var(--ink); white-space: nowrap; text-transform: uppercase;
  }
  .company-name__accent { color: var(--teal); }
  .front__band {
    position: absolute; left: 0; top: 172px; width: 100%; height: 236px;
    background: var(--teal);
  }
  .person-name {
    position: absolute; right: 58px; top: 14px;
    color: var(--paper); font-weight: 700; font-size: 31px;
  }
  .contact {
    position: absolute; display: flex; align-items: center; gap: 12px;
    color: var(--paper); font-size: 27px; white-space: nowrap;
  }
  .contact__badge {
    width: 26px; height: 26px; border-radius: 5px;
    background: var(--paper); color: var(--teal);
    font-weight: 700; font-size: 18px;
    display: flex; align-items: center; justify-content: center;
  }
  .contact--address { left: 58px; top: 76px; }
  .contact--office  { left: 58px; top: 130px; }
  .contact--fax     { left: 480px; top: 130px; }
  .contact--mobile  { left: 58px; top: 184px; }
  .contact--email   { left: 480px; top: 184px; }
  .front__footer {
    position: absolute; left: 0; top: 408px; width: 100%; height: 106px;
    background: linear-gradient(180deg, var(--paper) 0%, var(--paper-shade) 100%);
  }
  .website-line {
    position: absolute; left: 330px; top: 14px;
    display: flex; align-items: center; gap: 10px;
    color: var(--teal); font-weight: 700; font-size: 27px;
  }

  /* Back */
  .back__name {
    position: absolute; left: 0; top: 118px; width: 100%; text-align: center;
    font-family: "Roboto Condensed", "Arial Narrow", sans-serif;
    font-weight: 400; font-size: 50px; color: var(--paper);
    text-transform: uppercase; letter-spacing: 0.5px;
  }
  .back__website {
    position: absolute; left: 50%; top: 226px; transform: translateX(-50%);
    background: var(--paper); color: var(--teal);
    border-radius: 10px; padding: 6px 22px;
    font-weight: 700; font-size: 27px; white-space: nowrap;
  }
  .social-strip {
    position: absolute; right: 0; bottom: 0; width: 360px; height: 74px;
    background: var(--paper);
    clip-path: polygon(40px 0, 100% 0, 100% 100%, 0 100%);
    display: flex; align-items: center; justify-content: flex-end;
    gap: 12px; padding-right: 26px;
  }
  .social-strip__label { color: var(--teal); font-weight: 700; font-size: 26px; margin-right: 8px; }
  .social-strip__dot { width: 24px; height: 24px; border-radius: 50%; background: var(--teal); }
</style>
</head>
<body>

<section class="card card--front" aria-label="Business card front">
  <div class="front__header"></div>
  <div class="front__accent"></div>
  <h1 class="company-name">Oak &amp; Meridian <span class="company-name__accent">Contracting</span></h1>

  <div class="front__band">
    <p class="person-name">Dominic Valtersen</p>
    <p class="contact contact--address"><span class="contact__badge">A</span>318 fenwick st kellerton ny 10618</p>
    <p class="contact contact--office"><span class="contact__badge">T</span>914-208-3916</p>
    <p class="contact contact--fax"><span class="contact__badge">F</span>914-208-5523</p>
    <p class="contact contact--mobile"><span class="contact__badge">M</span>917-526-0389</p>
    <p class="contact contact--email"><span class="contact__badge">E</span>harborkeybuild@mailbrook.com</p>
  </div>

  <div class="front__footer">
    <p class="website-line">
      <svg width="24" height="24" viewBox="0 0 24 24" aria-hidden="true">
        <g fill="none" stroke="#1cb8a2" stroke-width="2">
          <circle cx="12" cy="12" r="10"/>
          <ellipse cx="12" cy="12" rx="4.5" ry="10"/>
          <line x1="2" y1="12" x2="22" y2="12"/>
        </g>
      </svg>
      www.harborkeybuild.com
    </p>
  </div>
</section>

<section class="card card--back" aria-label="Business card back">
  <h2 class="back__name">Oak &amp; Meridian Contracting</h2>
  <p class="back__website">www.harborkeybuild.com</p>
  <div class="social-strip">
    <span class="social-strip__label">Follow us on</span>
    <span class="social-strip__dot"></span>
    <span class="social-strip__dot"></span>
    <span class="social-strip__dot"></span>
    <span class="social-strip__dot"></span>
  </div>
</section>

</body>
</html>
```